Architectural Design Brochure

I need you to design 5 pages (they will be used as templates which I can then edit later).

Please design 5 pages - copy the example pdf provided as reference (Morrow Fold). Please copy pages 1,3,5,6,7 from the example provided. But make the style match my unique brand. I want the layout to be similar to the example but still must be unique - use my logo and brand style blue, white, silver and grey.

I must be able to edit the brochure myself after you have finished these 5 pages (to change text and images etc) so it must be given to me in suitable format which I can edit in (psd or gimp).

my website is www.plenwick.com.au
my logo is attached

Target Market(s)

Home Builders and Architects

Requirements
Must have
• I would like you to design it around my brand - white, blue, grey and silver.

Must do 5 pages, copy the layout as shown in the example Morrow Fold pdf - I need pages 1,3,5,6,7
Nice to have
• Unique stlye
same layout as example - pages 1,3,5,6,7
Should not have
• Should not be exactly same style / watermarks etc as example

```html
<!DOCTYPE html>
<html lang="en">
<head>
<meta charset="utf-8">
<title>Plenwick – Contact Page</title>
<link rel="stylesheet" href="https://fonts.googleapis.com/css2?family=Arimo:wght@400;700&display=swap">
<style>
  :root {
    --paper: #ffffff;
    --slate: #4a5058;
    --brand-blue: #3f8acb;
    --brand-grey: #4b4d50;
    --text-light: #ffffff;
  }
  html, body {
    margin: 0;
    padding: 0;
    overflow: hidden;
    background: var(--paper);
  }
  .page {
    position: relative;
    width: 927px;
    height: 1200px;
    overflow: hidden;
    background: var(--paper);
    font-family: "Arimo", Helvetica, Arial, sans-serif;
  }
  .brand {
    position: absolute;
    top: 148px;
    right: 85px;
    display: flex;
    align-items: center;
    gap: 14px;
  }
  .brand-mark {
    width: 52px;
    height: 52px;
    background: var(--brand-blue);
  }
  .brand-name {
    font-size: 58px;
    font-weight: 700;
    letter-spacing: 1px;
    color: var(--brand-grey);
    line-height: 1;
  }
  .band-office {
    position: absolute;
    left: 0;
    top: 258px;
    width: 100%;
    height: 159px;
    background: var(--slate);
  }
  .band-team {
    position: absolute;
    left: 0;
    top: 417px;
    width: 100%;
    height: 674px;
    background: var(--brand-blue);
  }
  .contact-list {
    position: absolute;
    right: 85px;
    margin: 0;
    text-align: right;
    color: var(--text-light);
    font-size: 18px;
    line-height: 23px;
  }
  .contact-list dt,
  .contact-list dd {
    margin: 0;
  }
  .contact-list dd + dt {
    margin-top: 19px;
  }
  .contact-office { top: 285px; }
  .contact-team { top: 438px; }
</style>
</head>
<body>
<main class="page">
  <header class="brand">
    <span class="brand-mark"></span>
    <span class="brand-name">Plenwick</span>
  </header>

  <section class="band-office">
    <dl class="contact-list contact-office" style="top:27px">
      <dt>Telephone:</dt>
      <dd>1300 555 214</dd>
      <dt>Email (Inquiries):</dt>
      <dd>info@plenwick.com.au</dd>
    </dl>
  </section>

  <section class="band-team">
    <dl class="contact-list contact-team" style="top:21px">
      <dt>Tom Hadley (Mobile):</dt>
      <dd>0400 555 128</dd>
      <dt>Sam Prewitt (Mobile):</dt>
      <dd>0400 555 397</dd>
    </dl>
  </section>
</main>
</body>
</html>
```